Koozie/Can Cooler Vector One Color Logo Design for car event Austin Chicago

We need a vector-based one color design for the front, back, and bottom of a koozie. This requires
. The koozie is for a car event. There is a car rally which starts in Austin, Texas and ends in Chicago Illinois. Both cities and states should be represented along with the website of "RoadWingTrail.com". The dates of the event must also be included: August 4th-10th 2014. The event is tailored to a large number of high performance sports cars which travel along back roads, highways, and scenic routes across the United States. Previous routes have been Dallas to Miami which I have attached a file showing a similar proof that merged the oil of Texas, with the palms of Florida, using a deco design.

We are seeking a design with inspiration from both Austin & Chicago, motor racing, fast & exotic automobiles, using a clean yet creative design.

Target Market(s)

Rich men who drive fast cars.

Industry/Entity Type

Travel

Font styles to use
Serif
Sans Serif
Decorative

Requirements
Must have
• -Relate to both Austin, Texas & Chicago, Illinois.
-RoadWingTrail.com text
-August 4th-10th text
-Glimmerway Rally text
-Two separate vector images of 3x3" and another of 2"x1"
-Two tone color; black & white
Nice to have
• Clean design due to small print area.
Commonality between three vectors.
Should not have
• Hard to read text. Overly detailed design aspects.

```html
<!DOCTYPE html>
<html lang="en">
<head>
<meta charset="utf-8">
<title>Austin to Chicago Rally Koozie</title>
<link rel="stylesheet" href="https://fonts.googleapis.com/css2?family=Fraunces:opsz,wght@144,900&family=Oswald:wght@600&display=swap">
<style>
  :root {
    --backdrop: #ffffff;
    --ink: #141414;
    --paper: #ffffff;
  }
  * { margin: 0; padding: 0; box-sizing: border-box; }
  html, body {
    width: 1200px;
    height: 900px;
    overflow: hidden;
    background: var(--backdrop);
  }
  .koozie-face {
    position: absolute;
    left: 198px;
    top: 52px;
    width: 792px;
    height: 791px;
    background: var(--paper);
    color: var(--ink);
  }
  .city {
    position: absolute;
    left: 0;
    width: 100%;
    text-align: center;
    font-family: "Fraunces", "Georgia", serif;
    font-weight: 900;
    font-style: normal;
    line-height: 1;
    letter-spacing: -1px;
  }
  .city-start { top: 60px; font-size: 104px; }
  .city-end { top: 410px; font-size: 124px; }
  .car-art {
    position: absolute;
    left: 140px;
    top: 192px;
    width: 510px;
    height: 218px;
    border-radius: 40% 45% 20% 20% / 50% 50% 30% 30%;
    background: var(--ink);
  }
  .event-info {
    position: absolute;
    left: 0;
    top: 566px;
    width: 100%;
    text-align: center;
    font-family: "Oswald", "Arial Narrow", sans-serif;
    font-weight: 600;
    line-height: 1.12;
  }
  .event-dates { font-size: 48px; letter-spacing: 0.5px; }
  .event-site { font-size: 54px; letter-spacing: 0.3px; }
  .event-name { font-size: 30px; letter-spacing: 1px; margin-top: 4px; }
  .flag {
    position: absolute;
    top: 605px;
    width: 115px;
    height: 76px;
  }
  .flag-chicago { left: 17px; }
  .flag-texas { left: 657px; }
</style>
</head>
<body>
  <main class="koozie-face">
    <h1 class="city city-start">Austin</h1>
    <div class="car-art" role="img" aria-label="Illustration of a sports car with flame decals trailing flames behind it"></div>
    <h2 class="city city-end">Chicago</h2>

    <svg class="flag flag-chicago" viewBox="0 0 115 76" aria-label="Chicago city flag">
      <rect x="0.5" y="0.5" width="114" height="75" fill="var(--paper)" stroke="var(--ink)"/>
      <rect x="1" y="13" width="113" height="12" fill="var(--ink)"/>
      <rect x="1" y="51" width="113" height="12" fill="var(--ink)"/>
      <g fill="var(--ink)" font-family="Arial, sans-serif" font-size="17" text-anchor="middle">
        <text x="24" y="44">✶</text>
        <text x="45" y="44">✶</text>
        <text x="67" y="44">✶</text>
        <text x="89" y="44">✶</text>
      </g>
    </svg>

    <div class="event-info">
      <p class="event-dates">August 4th-10th 2014</p>
      <p class="event-site">RoadWingTrail.com</p>
      <p class="event-name">Glimmerway Rally</p>
    </div>

    <svg class="flag flag-texas" viewBox="0 0 115 76" aria-label="Historic Texas flag">
      <rect x="0" y="0" width="115" height="76" fill="var(--ink)"/>
      <rect x="44" y="25" width="71" height="26" fill="var(--paper)"/>
      <g fill="var(--paper)" font-family="Arial, sans-serif" font-size="11" text-anchor="middle">
        <text x="22" y="15">★</text>
        <text x="33" y="21">★</text>
        <text x="11" y="21">★</text>
        <text x="35" y="36">★</text>
        <text x="9" y="36">★</text>
        <text x="29" y="50">★</text>
        <text x="15" y="50">★</text>
      </g>
    </svg>
  </main>
</body>
</html>
```